TESOL in Vietnam

My company needs banner ad designs (5 different sizes) to be placed on various websites to promote our product.

Our product is a 4-week Teaching English to Speakers of other Languages (TESOL) training program in Ho Chi Minh City, Vietnam. TESOL certification is the minimum qualification to work as an English language teacher in many parts of the world.

Basically, we want people to enroll in our 4 week Teacher training course in HCMC, Vietnam, with the view of teaching English in Vietnam.

You can see who we are and what we do here: www.brightlarklessons-asia.com

Key pointers include:

1. Our company logo (which includes our name & slogan) will be prominent in the banner - see attached

2. Our website address will be prominent:
www.brightlarklessons-asia.com

3. The main selling points for our product will be listed in the banner - note below:

Our TESOL training program in Ho Chi Minh City, Vietnam includes:

- the 4-week TESOL course (Australian Government accredited, internationally recognised);
- western standard accommodation within a 4 minute walk of my school for the duration of the course (4-weeks); and
- a guaranteed English teaching position at the end, paid at market rates.

4. the color scheme should be bright and eye catching - a lot of red, orange and alike.

I hope this information is helpful.

Martin Halloway

Hi All Note the rough sketch that I have added to the brief associated with this project. Cheers Martin

Target Market(s)

Men & women - 22 to 35 years of aage
Adventurous
Love to travel

Industry/Entity Type

Accommodation

Font styles to use
Other font styles liked:
• Calibri

Colors
eb1f27

Requirements
Must have
• Sense of fun
Credibility
Nice to have
• bright colors
Should not have
• Dour

```html
<!DOCTYPE html>
<html lang="en">
<head>
<meta charset="utf-8">
<title>TESOL in Vietnam – Banner Set</title>
<link rel="stylesheet" href="https://fonts.googleapis.com/css2?family=Open+Sans:wght@400;700&display=swap">
<style>
  :root {
    --brand-red: #eb1f27;
    --magenta: #c8177e;
    --pink: #e6166f;
    --plum: #a51a86;
    --crimson: #e3243f;
    --white: #ffffff;
    --sheet: #ffffff;
    --rule-grey: #bdbdbd;
  }
  * { box-sizing: border-box; margin: 0; padding: 0; }
  html, body { width: 1200px; height: 884px; overflow: hidden; background: var(--sheet); }
  body { position: relative; font-family: "Open Sans", Calibri, sans-serif; color: var(--white); }

  .banner {
    position: absolute;
    overflow: hidden;
    background:
      radial-gradient(ellipse 60% 45% at 15% 30%, rgba(227,36,63,0.85), transparent 70%),
      radial-gradient(ellipse 50% 60% at 85% 75%, rgba(230,22,111,0.8), transparent 70%),
      linear-gradient(135deg, var(--plum) 0%, var(--magenta) 40%, var(--pink) 70%, var(--plum) 100%);
  }
  .title { font-weight: 700; text-shadow: 0 1px 2px rgba(0,0,0,0.35); line-height: 1.15; }
  .url { text-shadow: 0 1px 1px rgba(0,0,0,0.3); }
  .url b { font-weight: 700; }

  /* brand mark: invented name + plain circle */
  .brand { display: flex; align-items: center; gap: 8px; color: var(--brand-red); font-weight: 700; line-height: 1.05; }
  .brand .dot { flex: none; border-radius: 50%; background: var(--brand-red); }

  /* skyscraper */
  .skyscraper { left: 36px; top: 36px; width: 159px; height: 774px; text-align: center;
    background:
      radial-gradient(ellipse 90% 18% at 30% 33%, rgba(227,36,63,0.9), transparent 70%),
      radial-gradient(ellipse 90% 20% at 80% 70%, rgba(230,22,111,0.8), transparent 70%),
      linear-gradient(180deg, var(--magenta) 0%, var(--plum) 50%, var(--magenta) 100%); }
  .skyscraper .cap { position: absolute; left: -20px; top: 0; width: 199px; height: 116px; background: var(--white);
    border-radius: 0 0 50% 50% / 0 0 36px 36px; display: flex; align-items: center; justify-content: center; }
  .skyscraper .cap .brand { font-size: 13px; }
  .skyscraper .cap .dot { width: 14px; height: 14px; }
  .skyscraper .title { position: absolute; top: 176px; left: 0; width: 100%; font-size: 25px; }
  .skyscraper .point { position: absolute; left: 0; width: 100%; font-size: 18px; line-height: 27px; }
  .skyscraper .url { position: absolute; top: 650px; left: 0; width: 100%; font-size: 16px; line-height: 24px; }

  /* leaderboard */
  .leaderboard { left: 214px; top: 44px; width: 954px; height: 119px; }
  .leaderboard .cap { position: absolute; left: 0; top: 0; width: 256px; height: 119px; background: var(--white);
    border-radius: 0 120px 120px 0 / 0 70px 70px 0; display: flex; align-items: center; padding-left: 14px; }
  .leaderboard .cap .brand { font-size: 17px; }
  .leaderboard .cap .dot { width: 18px; height: 18px; }
  .leaderboard .title { position: absolute; left: 264px; top: 18px; font-size: 36px; }
  .leaderboard .url { position: absolute; left: 264px; top: 70px; font-size: 18px; }
  .leaderboard .divider { position: absolute; left: 603px; top: 20px; width: 2px; height: 78px; background: var(--white); }
  .leaderboard .points { position: absolute; left: 616px; top: 20px; list-style: none; font-size: 17px; line-height: 27px; }

  /* small banner */
  .button-banner { left: 301px; top: 375px; width: 309px; height: 78px; text-align: center; }
  .button-banner .title { margin-top: 11px; font-size: 28px; }
  .button-banner .url { font-size: 15px; }

  /* medium rectangle */
  .rectangle { left: 704px; top: 234px; width: 396px; height: 329px; text-align: center; }
  .rectangle .cap { position: absolute; left: 18px; top: 0; width: 360px; height: 151px; background: var(--white);
    border-radius: 0 0 30px 30px; display: flex; align-items: center; justify-content: center; }
  .rectangle .cap .brand { font-size: 24px; }
  .rectangle .cap .dot { width: 26px; height: 26px; }
  .rectangle .title { position: absolute; top: 164px; left: 0; width: 100%; font-size: 31px; }
  .rectangle .url { position: absolute; top: 206px; left: 0; width: 100%; font-size: 17px; }
  .rectangle .points { position: absolute; top: 240px; left: 0; width: 100%; list-style: none; font-size: 17px; line-height: 28px; }

  /* bottom banner */
  .banner-wide { left: 317px; top: 653px; width: 612px; height: 78px; }
  .banner-wide .cap { position: absolute; left: 0; top: 0; width: 174px; height: 78px; background: var(--white);
    border-radius: 0 80px 80px 0 / 0 45px 45px 0; display: flex; align-items: center; padding-left: 8px; }
  .banner-wide .cap .brand { font-size: 13px; }
  .banner-wide .cap .dot { width: 14px; height: 14px; }
  .banner-wide .title { position: absolute; left: 185px; top: 4px; font-size: 35px; }
  .banner-wide .url { position: absolute; left: 215px; top: 48px; font-size: 18px; }

  .sheet-rule { position: absolute; left: 0; top: 853px; width: 1200px; height: 10px; background: var(--rule-grey); }
</style>
</head>
<body>

  <section class="banner skyscraper" aria-label="Skyscraper banner">
    <div class="cap"><div class="brand"><span class="dot"></span><span>Bright Lark<br>Lessons</span></div></div>
    <h2 class="title">TESOL in<br>Vietnam</h2>
    <p class="point" style="top:284px">Australian<br>Goverment<br>accredited</p>
    <p class="point" style="top:404px">FREE<br>accomm. in<br>Ho Chi Minh City</p>
    <p class="point" style="top:523px">Guaranteed<br>teaching job<br>at the end</p>
    <p class="url"><b>brightlark<br>lessons-asia</b>.com</p>
  </section>

  <section class="banner leaderboard" aria-label="Leaderboard banner">
    <div class="cap"><div class="brand"><span class="dot"></span><span>Bright Lark Lessons</span></div></div>
    <h2 class="title">TESOL in Vietnam</h2>
    <p class="url">www.<b>brightlarklessons-asia</b>.com</p>
    <span class="divider"></span>
    <ul class="points">
      <li>Australian Goverment accredited</li>
      <li>Free accommodation in Ho Chi Minh City</li>
      <li>Guaranteed teaching job at the end</li>
    </ul>
  </section>

  <section class="banner button-banner" aria-label="Small banner">
    <h2 class="title">TESOL in Vietnam</h2>
    <p class="url">www.<b>brightlarklessons-asia</b>.com</p>
  </section>

  <section class="banner rectangle" aria-label="Medium rectangle banner">
    <div class="cap"><div class="brand"><span class="dot"></span><span>Bright Lark Lessons</span></div></div>
    <h2 class="title">TESOL in Vietnam</h2>
    <p class="url">www.<b>brightlarklessons-asia</b>.com</p>
    <ul class="points">
      <li>• Australian Goverment accredited</li>
      <li>• Free accommodation in Ho Chi Minh City</li>
      <li>• Guaranteed teaching job at the end</li>
    </ul>
  </section>

  <section class="banner banner-wide" aria-label="Wide banner">
    <div class="cap"><div class="brand"><span class="dot"></span><span>Bright Lark Lessons</span></div></div>
    <h2 class="title">TESOL in Vietnam</h2>
    <p class="url">Visit www.<b>brightlarklessons-asia</b>.com</p>
  </section>

  <div class="sheet-rule"></div>
</body>
</html>
```